Packaging Design for Vanta Core

We require an outstanding packaging design for our Vanta Core brand, which offers hydration electrolyte supplements specifically tailored for athletes and sporty individuals.

Benchmark packaging design from liquora competitor attached. The product packaging contains 20 x 20g sticks of the product.

Target Market

Psychographic: Health-conscious, active lifestyle, values quality, functionality and sustainability.

product description 1:
HYDRATION BOOSTER
Refresh, Replenish, Recharge!

product description 2:
PREMIUM ISOTONIC ELECTROLYTE DRINK
Nutritional Expertise Since 1992.

Existing Logo: to add "since 1992"

Appeal to Target Market: Create a design that resonates with both men and women in the 25-55 age group.

Grafik Design: Develop a visually striking design that grabs attention in online retail environments like Brindle.

Visuals: glass of water (or symbolic) and sticks (powder) just like benchmark brand liquora.

Design Elements
Use colours that are inside the Vanta-Core Logo, attached.
Product will be available in 3 flavours. Lemon=yellow, Orange=orange, Black Currant=purple

Typography: Utilize strong, clean, and modern fonts. Ensure readability and create a sense of strength, endurance and reliability.

The product will be available in 3 flavours: Lemon, Orange and Johannisbeere

We look forward to seeing your creative ideas and innovative designs for our Vanta Core brand packaging.

```html
<!DOCTYPE html>
<html lang="en">
<head>
<meta charset="utf-8">
<title>Vanta Core – Hydration Booster Pack</title>
<link rel="stylesheet" href="https://fonts.googleapis.com/css2?family=Outfit:wght@700;800&display=swap">
<style>
  :root {
    --page-bg: #f4f4f4;
    --pack-white: #ffffff;
    --brand-magenta: #cc0060;
    --lemon-yellow: #fbe31a;
    --ink: #2a2a2a;
    --frame: #333333;
    --photo-light: #e4e7ec;
    --photo-mid: #c3c9d1;
  }
  * { margin: 0; padding: 0; box-sizing: border-box; }
  html, body {
    width: 1200px;
    height: 891px;
    overflow: hidden;
    background: var(--page-bg);
    font-family: "Outfit", Arial, sans-serif;
  }
  .canvas {
    position: relative;
    width: 1200px;
    height: 891px;
  }
  .pack-face {
    position: absolute;
    left: 398px;
    top: 232px;
    width: 391px;
    height: 423px;
    background: var(--pack-white);
    border: 1px solid var(--frame);
    overflow: hidden;
  }
  .band-flavour {
    position: absolute;
    left: 0; right: 0;
    top: 237px;
    height: 105px;
    background: var(--lemon-yellow);
  }
  .band-brand {
    position: absolute;
    left: 0; right: 0;
    top: 342px;
    bottom: 0;
    background: var(--brand-magenta);
  }
  .brand-name {
    position: absolute;
    left: 20px;
    top: 54px;
    display: flex;
    align-items: center;
    gap: 10px;
    color: var(--brand-magenta);
    font-weight: 800;
    font-size: 44px;
    line-height: 1;
    letter-spacing: -0.5px;
  }
  .brand-dot {
    width: 22px;
    height: 22px;
    border-radius: 50%;
    background: var(--brand-magenta);
  }
  .product-title {
    position: absolute;
    left: 22px;
    top: 188px;
    color: var(--ink);
    font-weight: 800;
    font-size: 28px;
    line-height: 0.9;
    letter-spacing: 0.2px;
    text-transform: uppercase;
  }
  .tagline {
    position: absolute;
    left: 22px;
    top: 279px;
    color: var(--pack-white);
    font-weight: 700;
    font-size: 13px;
    letter-spacing: 0.1px;
  }
  .glass-photo {
    position: absolute;
    left: 199px;
    top: 114px;
    width: 165px;
    height: 275px;
    background: linear-gradient(180deg, var(--photo-light), var(--photo-mid));
    opacity: 0.45;
  }
</style>
</head>
<body>
  <main class="canvas">
    <section class="pack-face">
      <div class="band-flavour"></div>
      <div class="band-brand"></div>

      <div class="brand-name"><span class="brand-dot"></span>Vanta Core</div>

      <h1 class="product-title">Hydration<br>Booster</h1>
      <p class="tagline">Refresh, Replenish, Recharge!</p>

      <div class="glass-photo" role="img" aria-label="Photo of a clear glass of water with splashing droplets"></div>
    </section>
  </main>
</body>
</html>
```